Brightmarrow4Pay Pty Ltd
CorporateTelecommunications Auditor & Leakage Expert
Korin Thewel
Managing Director
Unit 8 / 14 Pelham Rd Dunmore Vale VIC 3149
korin.thewel@brightmarrow4pay.com
Your CorporateTelecommunications Auditor & Leakage Expert

```html
<!DOCTYPE html>
<html lang="en">
<head>
<meta charset="utf-8">
<title>Brightmarrow4Pay Business Cards</title>
<link rel="stylesheet" href="https://fonts.googleapis.com/css2?family=Arimo:wght@400;700&display=swap">
<style>
  :root {
    --bg: #e4e2df;
    --card: #ffffff;
    --accent: #d7262e;
    --ink: #4a4a4a;
    --ink-soft: #7a7a7a;
    --rule: #cfcfcf;
    --wordmark: #3a3a3a;
  }
  * { box-sizing: border-box; margin: 0; padding: 0; }
  html, body {
    width: 1200px; height: 852px; overflow: hidden;
    background: var(--bg);
    font-family: "Arimo", Arial, sans-serif;
    color: var(--ink);
  }
  .canvas { position: relative; width: 1200px; height: 852px; }
  .card {
    position: absolute;
    width: 560px; height: 340px;
    background: var(--card);
    border-radius: 18px;
    box-shadow: 0 6px 18px rgba(0,0,0,0.18);
  }
  .card--landscape { left: 60px; top: 80px; }
  .card--stacked { left: 580px; top: 432px; }

  .wordmark {
    font-weight: 400;
    color: var(--wordmark);
    white-space: nowrap;
  }
  .card--landscape .wordmark {
    position: absolute; left: 0; right: 0; top: 96px;
    text-align: center; font-size: 34px;
  }

  .person-name { color: var(--accent); font-weight: 700; font-size: 17px; }
  .person-title { color: var(--ink-soft); font-size: 12px; margin-top: 3px; }
  .address { font-size: 12px; line-height: 1.45; margin-top: 14px; }

  .card--landscape .identity {
    position: absolute; left: 56px; top: 208px; width: 210px; text-align: right;
    padding-right: 18px;
  }
  .card--landscape .divider {
    position: absolute; left: 285px; top: 210px; width: 1px; height: 88px;
    background: var(--rule);
  }
  .card--landscape .contacts { position: absolute; left: 304px; top: 212px; }

  .contacts { list-style: none; font-size: 12px; }
  .contacts li { display: flex; align-items: center; gap: 8px; height: 20px; white-space: nowrap; }
  .contacts svg { width: 12px; height: 12px; flex: none; }

  .card--stacked .brand-block {
    position: absolute; left: 30px; top: 0; bottom: 0; width: 210px;
    display: flex; align-items: center; justify-content: center;
  }
  .card--stacked .wordmark { font-size: 22px; text-align: center; }
  .card--stacked .divider {
    position: absolute; left: 250px; top: 60px; width: 1px; height: 220px;
    background: var(--rule);
  }
  .card--stacked .details { position: absolute; left: 272px; top: 52px; }
  .card--stacked .contacts { margin-top: 22px; }
</style>
</head>
<body>
<main class="canvas">

  <section class="card card--landscape" aria-label="Business card, landscape layout">
    <div class="wordmark">Brightmarrow4Pay</div>
    <div class="identity">
      <p class="person-name">Korin Thewel</p>
      <p class="person-title">Managing Director</p>
      <p class="address">Unit 8 / 14 Pelham Rd<br>Dunmore Vale VIC 3149</p>
    </div>
    <div class="divider"></div>
    <ul class="contacts">
      <li><svg viewBox="0 0 12 12"><path d="M2 1h2.5l1 3-1.5 1a6 6 0 0 0 3 3l1-1.5 3 1V11h-1.5A9 9 0 0 1 1 2.5V1z" fill="#d7262e"/></svg>03 9555 0142</li>
      <li><svg viewBox="0 0 12 12"><rect x="3" y="0.5" width="6" height="11" rx="1.2" fill="#d7262e"/><rect x="4" y="2" width="4" height="7" fill="#fff"/></svg>0400 555 218</li>
      <li><svg viewBox="0 0 12 12"><rect x="0.5" y="2.5" width="11" height="7" rx="1" fill="#d7262e"/><path d="M1 3l5 4 5-4" stroke="#fff" fill="none"/></svg>korin.thewel@brightmarrow4pay.com</li>
      <li><svg viewBox="0 0 12 12"><circle cx="6" cy="6" r="5.5" fill="#d7262e"/><path d="M0.5 6h11M6 0.5c-3 3-3 8 0 11M6 0.5c3 3 3 8 0 11" stroke="#fff" stroke-width="0.8" fill="none"/></svg>www.brightmarrow4pay.com</li>
    </ul>
  </section>

  <section class="card card--stacked" aria-label="Business card, stacked layout">
    <div class="brand-block">
      <div class="wordmark">Brightmarrow4Pay</div>
    </div>
    <div class="divider"></div>
    <div class="details">
      <p class="person-name">Korin Thewel</p>
      <p class="person-title">Managing Director</p>
      <p class="address">Unit 8 / 14 Pelham Rd<br>Dunmore Vale VIC 3149</p>
      <ul class="contacts">
        <li><svg viewBox="0 0 12 12"><path d="M2 1h2.5l1 3-1.5 1a6 6 0 0 0 3 3l1-1.5 3 1V11h-1.5A9 9 0 0 1 1 2.5V1z" fill="#d7262e"/></svg>03 9555 0142</li>
        <li><svg viewBox="0 0 12 12"><rect x="3" y="0.5" width="6" height="11" rx="1.2" fill="#d7262e"/><rect x="4" y="2" width="4" height="7" fill="#fff"/></svg>0400 555 218</li>
        <li><svg viewBox="0 0 12 12"><rect x="0.5" y="2.5" width="11" height="7" rx="1" fill="#d7262e"/><path d="M1 3l5 4 5-4" stroke="#fff" fill="none"/></svg>korin.thewel@brightmarrow4pay.com</li>
        <li><svg viewBox="0 0 12 12"><circle cx="6" cy="6" r="5.5" fill="#d7262e"/><path d="M0.5 6h11M6 0.5c-3 3-3 8 0 11M6 0.5c3 3 3 8 0 11" stroke="#fff" stroke-width="0.8" fill="none"/></svg>www.brightmarrow4pay.com</li>
      </ul>
    </div>
  </section>

</main>
</body>
</html>
```